Rapid Surveillance Command Unit (RSCU) Design & Build

We need a product brochure for our custom design and built RSCU units. We build RSCU units for Government agencies, law enforcement providers, border protection agencies, private security organsiations and others. These are bespoke vehicles customised to a clients specific needs. We also make rapid deploy CCTV camera units for use with the vehicles or as a separate product.
I've included all the brochure info in the attached Word document as well as an array of photographs to choose from. Please look at our websites for further company image clarification. www.korvenda.com.au and korvendaplt.com.au
Product partners logos should be included. Ideally, the brochure should be double sided A4 size please.

Target Market(s)

Local, Federal, State and International Government Agencies, Dept of Justice, Prisons, Private Security Organisations.

Industry/Entity Type

Government

Other font styles liked:
• Helvetica

Colors
0292cd
000000
c3c3c3
0692cd
85cae6

Requirements
Must have
• Professional, bold appearance that matches our branding. These custom designed vehicles are expensive and our clients are very high end. The brochure must look and feel this way too
Should not have
• A generic look, must be unique

```html
<!DOCTYPE html>
<html lang="en">
<head>
<meta charset="utf-8">
<title>RSCU Brochure</title>
<link href="https://fonts.googleapis.com/css2?family=Roboto+Condensed:wght@400;500;700&family=Arimo:wght@400;700&display=swap" rel="stylesheet">
<style>
:root{
  --blue:#0292cd;
  --blue-deep:#0a5ea8;
  --navy:#124a8c;
  --sky:#85cae6;
  --grey:#c3c3c3;
  --stage:#c6c7c9;
  --ink:#2b2b2b;
  --white:#ffffff;
}
*{margin:0;padding:0;box-sizing:border-box}
html,body{width:1200px;height:782px;overflow:hidden}
body{background:var(--stage);font-family:"Arimo",Helvetica,Arial,sans-serif;color:var(--ink);position:relative}
.page{position:absolute;top:54px;width:528px;height:684px;background:var(--white);overflow:hidden}
.page-front{left:55px}
.page-back{left:621px}
.abs{position:absolute}
.photo{position:absolute}
.heading{font-family:"Roboto Condensed",Arial Narrow,sans-serif;color:var(--blue-deep);font-weight:500;white-space:nowrap}
.body-copy{font-size:8.6px;line-height:11.3px}
.brand{position:absolute;display:flex;align-items:center;gap:6px;font-family:"Arimo",Helvetica,sans-serif;font-weight:700;color:var(--blue-deep);white-space:nowrap}
.brand .dot{width:12px;height:12px;border-radius:50%;background:var(--blue)}
.title-bar{position:absolute;left:0;top:157px;width:528px;height:36px;background:linear-gradient(90deg,var(--blue-deep),var(--blue) 60%,#4fb1dc)}
.title-bar h1{font-family:"Roboto Condensed",sans-serif;font-weight:500;color:var(--white);font-size:17.5px;position:absolute;left:32px;top:8px;letter-spacing:.2px;white-space:nowrap}
.bullets{list-style:none;position:absolute}
.bullets li{position:relative;padding-left:19px;font-size:8.6px;line-height:11.3px;color:var(--ink)}
.bullets li svg{position:absolute;left:0;top:1px}
.footer{position:absolute;left:0;top:628px;width:528px;height:56px}
.footer .stripe{position:absolute;left:0;top:0;width:528px;height:6px;background:linear-gradient(90deg,#e6e6e6,var(--grey),#e6e6e6)}
.footer .band{position:absolute;left:0;top:6px;width:528px;height:50px;background:linear-gradient(90deg,var(--blue),var(--blue-deep) 70%,var(--navy))}
.footer .item{position:absolute;color:var(--white);font-size:9.5px;line-height:12px;white-space:nowrap}
.footer svg{position:absolute}
.info-box{position:absolute;left:18px;top:380px;width:301px;height:104px;background:linear-gradient(100deg,var(--blue),var(--blue-deep) 70%,var(--navy));color:var(--white);font-size:10px;line-height:12.4px;padding:13px 18px 0 19px}
.deploy-box{position:absolute;left:93px;top:506px;width:98px;height:85px;background:#58595b;color:var(--white);font-size:10px;line-height:12.3px;padding:6px 8px 0 12px}
.badge{position:absolute}
.contact-copy{position:absolute;left:342px;font-size:10px;line-height:12.4px;color:#333}
</style>
</head>
<body>

<section class="page page-front">
  <div class="photo" role="img" aria-label="City skyline at night with light trails" style="left:0;top:0;width:528px;height:157px;background:linear-gradient(180deg,#2a3a8a 0%,#5a4aa6 35%,#c78a6a 75%,#f1c48c 100%)"></div>
  <svg class="abs" style="left:0;top:0" width="260" height="157" viewBox="0 0 260 157">
    <polygon points="0,36 210,0 258,0 205,157 0,157" fill="#ffffff"/>
  </svg>
  <div class="brand" style="left:34px;top:96px;font-size:36px;letter-spacing:1px"><span class="dot"></span>RSCU</div>

  <div class="title-bar"><h1>RSCU- the Ultimate Rapid Surveillance Solution</h1></div>
  <div class="photo" role="img" aria-label="PTZ surveillance camera on a pole mount" style="left:418px;top:155px;width:72px;height:134px;background:linear-gradient(180deg,#e8eaee,#b9bfc7 60%,#dfe2e6);border-radius:18px 18px 4px 4px"></div>

  <p class="body-copy abs" style="left:34px;top:201px;width:372px">Korvenda Security Systems has 15 years' direct experience designing and installing state of the art, multi-faceted electronic security solutions across all business sectors throughout Australia. We designed and built the first RSCU as a hire service for event management companies however, its unique design features and our ability to customise the vehicle for use in literally any situation, has led to demand from Government agencies, emergency service providers and private security organisations around the Asia Pacific region to build units specifically for their needs.</p>

  <h2 class="heading abs" style="left:34px;top:297px;font-size:14.5px">Our standard RSCU has the following Imaging and Communications features:</h2>

  <div class="photo" role="img" aria-label="Command vehicle with trailer parked by the sea" style="left:35px;top:325px;width:169px;height:109px;background:linear-gradient(180deg,#6fa6d8 0%,#a9c9e4 45%,#2c3140 65%,#9a9a8a 100%)"></div>
  <div class="photo" role="img" aria-label="Vehicle control room with wall of monitors" style="left:216px;top:325px;width:135px;height:109px;background:linear-gradient(180deg,#1b1a1a,#3e4a5c 45%,#8a7a62 70%,#1c1c1c)"></div>
  <div class="photo" role="img" aria-label="Operator screens showing live camera feeds" style="left:362px;top:325px;width:132px;height:109px;background:linear-gradient(160deg,#0e1e3a,#2a6db0 50%,#8fc6ea 80%,#15223c)"></div>

  <ul class="bullets" style="left:35px;top:452px;width:250px">
    <li style="margin-bottom:13px"><svg width="10" height="10" viewBox="0 0 10 10"><path d="M1 5.5 4 8.5 9 1.5" fill="none" stroke="#0292cd" stroke-width="2"/></svg>HD Fixed, thermal, PTZ (pan, tilt &amp; zoom) and 360 degree 4K cameras</li>
    <li style="margin-bottom:13px"><svg width="10" height="10" viewBox="0 0 10 10"><path d="M1 5.5 4 8.5 9 1.5" fill="none" stroke="#0292cd" stroke-width="2"/></svg>8 x Vehicle roof -mounted HD cameras for 360-degree visibility with either stationary or mobile recording capabilities</li>
    <li><svg width="10" height="10" viewBox="0 0 10 10"><path d="M1 5.5 4 8.5 9 1.5" fill="none" stroke="#0292cd" stroke-width="2"/></svg>8 x Autonomous rapid deploy camera kits, specific for 15km range remote surveillance operations, streaming live footage to the RSCU over a private, secure network All kits have GPS tracking, integrated battery power, private Point-to-Multipoint (PTMP) wireless network link plus cloud connectivity over 3G/4G LTE networks, with up to 2 weeks' remote operational capability.</li>
  </ul>
  <ul class="bullets" style="left:312px;top:452px;width:180px">
    <li style="margin-bottom:11px"><svg width="10" height="10" viewBox="0 0 10 10"><path d="M1 5.5 4 8.5 9 1.5" fill="none" stroke="#0292cd" stroke-width="2"/></svg>Telescopic mast to 12.5m above vehicle equipped as standard with 2 x 180 degree fixed HD cameras and 1 x long range IR PTZ camera ideal for perimetre protection</li>
    <li style="margin-bottom:11px"><svg width="10" height="10" viewBox="0 0 10 10"><path d="M1 5.5 4 8.5 9 1.5" fill="none" stroke="#0292cd" stroke-width="2"/></svg>IP two-way PA systems</li>
    <li style="margin-bottom:11px"><svg width="10" height="10" viewBox="0 0 10 10"><path d="M1 5.5 4 8.5 9 1.5" fill="none" stroke="#0292cd" stroke-width="2"/></svg>On-board UHF2 way radio system</li>
    <li><svg width="10" height="10" viewBox="0 0 10 10"><path d="M1 5.5 4 8.5 9 1.5" fill="none" stroke="#0292cd" stroke-width="2"/></svg>5 Outdoor PoE networked horn speakers provide clear, long range speech for remote speaking in video surveillance applications</li>
  </ul>

  <footer class="footer">
    <div class="stripe"></div><div class="band"></div>
    <svg style="left:31px;top:23px" width="8" height="11" viewBox="0 0 8 11"><path d="M4 11C1.5 7.5 0 5.6 0 4a4 4 0 0 1 8 0c0 1.6-1.5 3.5-4 7z" fill="#fff"/><circle cx="4" cy="4" r="1.5" fill="#0a5ea8"/></svg>
    <div class="item" style="left:42px;top:22px">Suite 3, Level 12, 48 Harbour Lane,<br>Melbourne, Vic 3000</div>
    <svg style="left:229px;top:23px" width="8" height="9" viewBox="0 0 8 9"><path d="M2 0 3.5 2.5 2.4 3.6C3 5 4 6 5.4 6.6L6.5 5.5 8 7 6.8 9C3 8.4 0 5.4 0 1.2z" fill="#fff"/></svg>
    <div class="item" style="left:240px;top:22px">03 9000 4718<br>info@korvenda.com.au</div>
    <svg style="left:360px;top:36px" width="9" height="9" viewBox="0 0 9 9"><circle cx="4.5" cy="4.5" r="4" fill="none" stroke="#fff"/><path d="M.5 4.5h8M4.5.5v8" stroke="#fff" stroke-width=".8"/></svg>
    <div class="item" style="left:373px;top:34px">www.korvendaplt.com.au</div>
  </footer>
</section>

<section class="page page-back">
  <div class="photo" role="img" aria-label="Glass skyscrapers seen from below against blue sky" style="left:0;top:0;width:528px;height:136px;background:linear-gradient(180deg,#2f6eaa 0%,#7fb2dc 45%,#cfe5f5 70%,#3d6f9c 100%)"></div>
  <svg class="abs" style="left:316px;top:0" width="212" height="72" viewBox="0 0 212 72"><polygon points="12,0 212,0 212,58 0,72" fill="#ffffff"/></svg>
  <div class="brand" style="left:341px;top:14px;font-size:34px;letter-spacing:1px"><span class="dot"></span>RSCU</div>

  <h2 class="heading abs" style="left:29px;top:155px;font-size:14.5px">Recording and Viewing:</h2>
  <h2 class="heading abs" style="left:319px;top:155px;font-size:14.5px">Power &amp; Auxiliary Services:</h2>

  <ul class="bullets" style="left:36px;top:180px;width:260px">
    <li style="margin-bottom:11px"><svg width="10" height="10" viewBox="0 0 10 10"><path d="M1 5.5 4 8.5 9 1.5" fill="none" stroke="#0292cd" stroke-width="2"/></svg>A 2- person control room with observation area</li>
    <li style="margin-bottom:13px"><svg width="10" height="10" viewBox="0 0 10 10"><path d="M1 5.5 4 8.5 9 1.5" fill="none" stroke="#0292cd" stroke-width="2"/></svg>GPS tracking &amp; video remote viewing<br>capability onsite or cloud based</li>
    <li style="margin-bottom:11px"><svg width="10" height="10" viewBox="0 0 10 10"><path d="M1 5.5 4 8.5 9 1.5" fill="none" stroke="#0292cd" stroke-width="2"/></svg>6 x 21" HD LCD monitors, 2 x 28' 4K LCD monitors &amp; on-board recording system</li>
    <li style="margin-bottom:11px"><svg width="10" height="10" viewBox="0 0 10 10"><path d="M1 5.5 4 8.5 9 1.5" fill="none" stroke="#0292cd" stroke-width="2"/></svg>VCA (Video Content Analytics) for any event</li>
    <li style="margin-bottom:11px"><svg width="10" height="10" viewBox="0 0 10 10"><path d="M1 5.5 4 8.5 9 1.5" fill="none" stroke="#0292cd" stroke-width="2"/></svg>Live streaming for effective event and incident management</li>
    <li><svg width="10" height="10" viewBox="0 0 10 10"><path d="M1 5.5 4 8.5 9 1.5" fill="none" stroke="#0292cd" stroke-width="2"/></svg>Vantrel VMS Security Centre, Norlink communications Camera Station, Skyward Networks cloud VMS &amp; Trackwise incident management software</li>
  </ul>

  <ul class="bullets" style="left:321px;top:182px;width:185px">
    <li style="margin-bottom:11px"><svg width="10" height="10" viewBox="0 0 10 10"><path d="M1 5.5 4 8.5 9 1.5" fill="none" stroke="#0292cd" stroke-width="2"/></svg>Complete standalone power source</li>
    <li style="margin-bottom:12px"><svg width="10" height="10" viewBox="0 0 10 10"><path d="M1 5.5 4 8.5 9 1.5" fill="none" stroke="#0292cd" stroke-width="2"/></svg>Generator for continuous power/ mains power capabilities</li>
    <li style="margin-bottom:12px"><svg width="10" height="10" viewBox="0 0 10 10"><path d="M1 5.5 4 8.5 9 1.5" fill="none" stroke="#0292cd" stroke-width="2"/></svg>Battery power to run for up to 24 hrs. (solar boosted)</li>
    <li><svg width="10" height="10" viewBox="0 0 10 10"><path d="M1 5.5 4 8.5 9 1.5" fill="none" stroke="#0292cd" stroke-width="2"/></svg>Equipped with air conditioning, refrigerator and built in storage</li>
  </ul>

  <div class="photo" role="img" aria-label="Command van with raised mast parked on a street" style="left:328px;top:310px;width:183px;height:177px;background:linear-gradient(180deg,#9cc3e6 0%,#c9dced 40%,#23262d 62%,#8d8f92 100%)"></div>

  <div class="info-box">RSCU vehicles are available for individual design and purchase. The units are fully customisable beyond the addition of CCTV equipment from leading IP networking manufacturers Norlink Communications, to include industry or agency specific communications and monitoring apparatus.</div>

  <div class="photo" role="img" aria-label="Rapid deploy camera unit on a roadside pole" style="left:20px;top:506px;width:73px;height:85px;background:linear-gradient(180deg,#b9d2e6,#7d8c76 55%,#505357)"></div>
  <div class="deploy-box">Rapid deploy camera units are also available with a wide variety of camera options</div>

  <div class="badge" role="img" aria-label="Partner badge" style="left:211px;top:509px;width:35px;height:36px;background:linear-gradient(180deg,#e9f2f8 50%,#2a6aa8 50%)"></div>
  <div class="badge" role="img" aria-label="Authorised partner badge" style="left:267px;top:507px;width:48px;height:38px;border:1px solid #9a8b7a;background:linear-gradient(180deg,#ffffff 55%,#9a8b7a 55%)"></div>
  <div class="badge" role="img" aria-label="Software partner badge" style="left:209px;top:565px;width:102px;height:30px;border-top:4px solid #9a9a9a;border-bottom:3px solid #f08a1c;background:#fbfbfb"></div>

  <p class="contact-copy" style="top:507px;width:175px">Consultations are essential.<br>Visit korvendaplt.com.au for more information and come and see an RSCU demonstration for yourself.</p>
  <p class="contact-copy" style="top:569px;width:175px">RSCU Factory: 4/12 Harlow Road,<br>Westmere, Vic 3049<br><span style="font-size:9px">(by appointment only)</span></p>

  <footer class="footer">
    <div class="stripe"></div><div class="band"></div>
    <svg style="left:31px;top:23px" width="8" height="11" viewBox="0 0 8 11"><path d="M4 11C1.5 7.5 0 5.6 0 4a4 4 0 0 1 8 0c0 1.6-1.5 3.5-4 7z" fill="#fff"/><circle cx="4" cy="4" r="1.5" fill="#0a5ea8"/></svg>
    <div class="item" style="left:42px;top:22px">Suite 3, Level 12, 48 Harbour Lane,<br>Melbourne, Vic 3000</div>
    <svg style="left:229px;top:23px" width="8" height="9" viewBox="0 0 8 9"><path d="M2 0 3.5 2.5 2.4 3.6C3 5 4 6 5.4 6.6L6.5 5.5 8 7 6.8 9C3 8.4 0 5.4 0 1.2z" fill="#fff"/></svg>
    <div class="item" style="left:240px;top:22px">03 9000 4718<br>info@korvenda.com.au</div>
    <svg style="left:360px;top:36px" width="9" height="9" viewBox="0 0 9 9"><circle cx="4.5" cy="4.5" r="4" fill="none" stroke="#fff"/><path d="M.5 4.5h8M4.5.5v8" stroke="#fff" stroke-width=".8"/></svg>
    <div class="item" style="left:373px;top:34px">www.korvendaplt.com.au</div>
  </footer>
</section>

</body>
</html>
```